Accounting Business needs double sided DL flyer design

We need a double sided DL flyer designed,
Front side with logo, web address and our short intro.
Backside to have a list of services.
Our colours are blue and a concrete grey colour. Look at our website for a feel for our colour scheme.
www.lanternwellgroup.com.au
I have included the pic from our website to possibly use but we are also open to new creative ideas.
Target Market(s)
Our target market are proactive business owners, particularly in the wine and hospitality industry.
Industry/Entity Type
Business
Look and feel

```html
<!DOCTYPE html>
<html lang="en">
<head>
<meta charset="utf-8">
<title>Lanternwell Group – DL Flyer</title>
<link rel="stylesheet" href="https://fonts.googleapis.com/css2?family=Anton&family=PT+Sans:wght@400;700&family=Saira:wght@700&display=swap">
<style>
  :root {
    --backdrop: #2b2b2b;
    --brand-blue: #1e4f97;
    --brand-blue-dark: #173f7d;
    --brand-blue-light: #2a67b8;
    --concrete: #7a7a7a;
    --concrete-dark: #5f5f5f;
    --ink: #1d2230;
    --paper: #ffffff;
    --paper-grey: #e9e9ea;
  }
  * { box-sizing: border-box; margin: 0; padding: 0; }
  html, body { width: 1200px; height: 1200px; overflow: hidden; }
  body { background: var(--backdrop); position: relative; font-family: "PT Sans", sans-serif; }

  .flyer { position: absolute; top: 125px; width: 475px; height: 977px; overflow: hidden; }
  .flyer--front { left: 97px; background: var(--paper); }
  .flyer--back { left: 630px; background: var(--paper-grey); }
  .flyer__art { position: absolute; inset: 0; width: 100%; height: 100%; }

  .brand { position: absolute; display: flex; align-items: center; gap: 12px; }
  .brand__mark { width: 46px; height: 46px; border-radius: 4px; flex: none; }
  .brand__name { font-family: "Saira", sans-serif; font-weight: 700; font-size: 28px; letter-spacing: 1px; line-height: 1; }
  .brand__tag { font-family: "PT Sans", sans-serif; font-size: 10.5px; letter-spacing: 3.6px; margin-top: 8px; }
  .brand--top { left: 37px; top: 50px; color: var(--brand-blue); }
  .brand--top .brand__mark { background: var(--brand-blue); }
  .brand--band { left: 30px; top: 720px; color: var(--paper); }
  .brand--band .brand__mark { background: var(--paper); }

  .tick { width: 22px; height: 22px; flex: none; }

  .promise { position: absolute; left: 47px; top: 560px; list-style: none; color: var(--paper); }
  .promise li { display: flex; align-items: center; gap: 12px; height: 48px; font-weight: 700; font-size: 30px; }
  .promise .tick { width: 20px; height: 20px; }

  .headline { position: absolute; left: 45px; top: 700px; font-family: "Anton", sans-serif; font-size: 104px; line-height: 1; color: var(--paper); letter-spacing: 1px; }

  .contact { position: absolute; left: 0; right: 0; top: 872px; text-align: center; color: var(--paper); }
  .contact__phone { display: flex; justify-content: center; align-items: center; gap: 8px; font-weight: 700; font-size: 33px; line-height: 40px; }
  .contact__phone svg { width: 20px; height: 22px; }
  .contact__web { display: flex; justify-content: center; align-items: center; gap: 6px; font-size: 20px; margin-top: 8px; }
  .contact__web svg { width: 13px; height: 13px; }

  .services__title { position: absolute; left: 26px; top: 28px; font-family: "Anton", sans-serif; font-size: 44px; line-height: 52px; color: var(--brand-blue); }
  .services { position: absolute; left: 31px; top: 89px; width: 440px; list-style: none; color: var(--ink); }
  .services li { display: flex; gap: 16px; font-size: 27px; line-height: 36px; margin-bottom: 12.8px; }
  .services .tick { margin-top: 7px; }
</style>
</head>
<body>

<section class="flyer flyer--front">
  <svg class="flyer__art" viewBox="0 0 594 1221" preserveAspectRatio="none">
    <defs>
      <linearGradient id="sky" x1="0" y1="0" x2="0" y2="1">
        <stop offset="0" stop-color="#ffffff"/>
        <stop offset="0.25" stop-color="#e4e8f4"/>
        <stop offset="0.5" stop-color="#f4f1e4"/>
        <stop offset="0.68" stop-color="#8a8578"/>
        <stop offset="0.8" stop-color="#2a2623"/>
        <stop offset="1" stop-color="#161515"/>
      </linearGradient>
      <linearGradient id="blueFront" x1="0" y1="0" x2="1" y2="0">
        <stop offset="0" stop-color="#1a4a8f"/>
        <stop offset="0.6" stop-color="#2766b6"/>
        <stop offset="1" stop-color="#1b4d95"/>
      </linearGradient>
      <linearGradient id="greyFront" x1="0" y1="0" x2="1" y2="0">
        <stop offset="0" stop-color="#6c6c6c"/>
        <stop offset="0.5" stop-color="#8a8a8a"/>
        <stop offset="1" stop-color="#646464"/>
      </linearGradient>
    </defs>
    <polygon points="0,150 594,150 594,625 0,700" fill="url(#sky)" role="img" aria-label="Photo: a figure holding a flag on a mountain summit at sunrise"/>
    <polygon points="0,688 594,613 594,1221 0,1221" fill="#ffffff"/>
    <polygon points="0,697 594,622 594,1005 0,1073" fill="url(#blueFront)"/>
    <polygon points="0,1084 594,1016 594,1221 0,1221" fill="url(#greyFront)"/>
  </svg>

  <div class="brand brand--top">
    <span class="brand__mark"></span>
    <div>
      <div class="brand__name">LANTERNWELL GROUP</div>
      <div class="brand__tag">BUSINESS ADVISORS &amp; ACCOUNTANTS</div>
    </div>
  </div>

  <ul class="promise">
    <li><svg class="tick" viewBox="0 0 22 22"><rect x="1" y="5" width="15" height="15" fill="none" stroke="#fff" stroke-width="2"/><path d="M5 12l4 4 11-13" fill="none" stroke="#fff" stroke-width="3"/></svg>A guiding hand</li>
    <li><svg class="tick" viewBox="0 0 22 22"><rect x="1" y="5" width="15" height="15" fill="none" stroke="#fff" stroke-width="2"/><path d="M5 12l4 4 11-13" fill="none" stroke="#fff" stroke-width="3"/></svg>A voice of reason</li>
    <li><svg class="tick" viewBox="0 0 22 22"><rect x="1" y="5" width="15" height="15" fill="none" stroke="#fff" stroke-width="2"/><path d="M5 12l4 4 11-13" fill="none" stroke="#fff" stroke-width="3"/></svg>A true sounding board for</li>
  </ul>
  <div class="headline">SUCCESS</div>

  <div class="contact">
    <div class="contact__phone"><svg viewBox="0 0 20 22"><path d="M4 2l4 4-2 3c1 3 3 6 6 8l3-2 4 4-3 3C8 21 1 12 1 5z" fill="#fff"/></svg>0400 123 987</div>
    <div class="contact__web"><svg viewBox="0 0 13 13"><circle cx="6.5" cy="6.5" r="6" fill="#fff"/></svg>www.lanternwellgroup.com.au</div>
  </div>
</section>

<section class="flyer flyer--back">
  <svg class="flyer__art" viewBox="0 0 594 1221" preserveAspectRatio="none">
    <defs>
      <linearGradient id="paperBack" x1="0" y1="0" x2="1" y2="0">
        <stop offset="0" stop-color="#e6e6e7"/>
        <stop offset="0.6" stop-color="#f7f7f7"/>
        <stop offset="1" stop-color="#dedede"/>
      </linearGradient>
      <linearGradient id="blueBack" x1="0" y1="0" x2="1" y2="0">
        <stop offset="0" stop-color="#1a4a8f"/>
        <stop offset="0.6" stop-color="#2766b6"/>
        <stop offset="1" stop-color="#1b4d95"/>
      </linearGradient>
      <linearGradient id="greyBack" x1="0" y1="0" x2="1" y2="0">
        <stop offset="0" stop-color="#6c6c6c"/>
        <stop offset="0.5" stop-color="#8a8a8a"/>
        <stop offset="1" stop-color="#646464"/>
      </linearGradient>
    </defs>
    <rect width="594" height="1221" fill="url(#paperBack)"/>
    <polygon points="0,868 594,808 594,1221 0,1221" fill="#ffffff"/>
    <polygon points="0,878 594,818 594,1002 0,1070" fill="url(#blueBack)"/>
    <polygon points="0,1082 594,1014 594,1221 0,1221" fill="url(#greyBack)"/>
  </svg>

  <h2 class="services__title">OUR SERVICES</h2>
  <ul class="services">
    <li><svg class="tick" viewBox="0 0 22 22"><rect x="1" y="5" width="15" height="15" fill="none" stroke="#1e4f97" stroke-width="2"/><path d="M5 12l4 4 11-13" fill="none" stroke="#1e4f97" stroke-width="3"/></svg>Taxation Compliance</li>
    <li><svg class="tick" viewBox="0 0 22 22"><rect x="1" y="5" width="15" height="15" fill="none" stroke="#1e4f97" stroke-width="2"/><path d="M5 12l4 4 11-13" fill="none" stroke="#1e4f97" stroke-width="3"/></svg><span>Financial &amp; Management<br>Reporting</span></li>
    <li><svg class="tick" viewBox="0 0 22 22"><rect x="1" y="5" width="15" height="15" fill="none" stroke="#1e4f97" stroke-width="2"/><path d="M5 12l4 4 11-13" fill="none" stroke="#1e4f97" stroke-width="3"/></svg>Self-Managed Superannuation</li>
    <li><svg class="tick" viewBox="0 0 22 22"><rect x="1" y="5" width="15" height="15" fill="none" stroke="#1e4f97" stroke-width="2"/><path d="M5 12l4 4 11-13" fill="none" stroke="#1e4f97" stroke-width="3"/></svg>Virtual CFO</li>
    <li><svg class="tick" viewBox="0 0 22 22"><rect x="1" y="5" width="15" height="15" fill="none" stroke="#1e4f97" stroke-width="2"/><path d="M5 12l4 4 11-13" fill="none" stroke="#1e4f97" stroke-width="3"/></svg>Business Planning</li>
    <li><svg class="tick" viewBox="0 0 22 22"><rect x="1" y="5" width="15" height="15" fill="none" stroke="#1e4f97" stroke-width="2"/><path d="M5 12l4 4 11-13" fill="none" stroke="#1e4f97" stroke-width="3"/></svg>KPIs&amp; Performance Monitoring</li>
    <li><svg class="tick" viewBox="0 0 22 22"><rect x="1" y="5" width="15" height="15" fill="none" stroke="#1e4f97" stroke-width="2"/><path d="M5 12l4 4 11-13" fill="none" stroke="#1e4f97" stroke-width="3"/></svg>Succession Planning</li>
    <li><svg class="tick" viewBox="0 0 22 22"><rect x="1" y="5" width="15" height="15" fill="none" stroke="#1e4f97" stroke-width="2"/><path d="M5 12l4 4 11-13" fill="none" stroke="#1e4f97" stroke-width="3"/></svg>Estate Planning</li>
    <li><svg class="tick" viewBox="0 0 22 22"><rect x="1" y="5" width="15" height="15" fill="none" stroke="#1e4f97" stroke-width="2"/><path d="M5 12l4 4 11-13" fill="none" stroke="#1e4f97" stroke-width="3"/></svg>Cloud Solutions</li>
    <li><svg class="tick" viewBox="0 0 22 22"><rect x="1" y="5" width="15" height="15" fill="none" stroke="#1e4f97" stroke-width="2"/><path d="M5 12l4 4 11-13" fill="none" stroke="#1e4f97" stroke-width="3"/></svg>Business Support Services</li>
    <li><svg class="tick" viewBox="0 0 22 22"><rect x="1" y="5" width="15" height="15" fill="none" stroke="#1e4f97" stroke-width="2"/><path d="M5 12l4 4 11-13" fill="none" stroke="#1e4f97" stroke-width="3"/></svg>The Wine Industry</li>
  </ul>

  <div class="brand brand--band">
    <span class="brand__mark"></span>
    <div>
      <div class="brand__name">LANTERNWELL GROUP</div>
      <div class="brand__tag">BUSINESS ADVISORS &amp; ACCOUNTANTS</div>
    </div>
  </div>

  <div class="contact">
    <div class="contact__phone"><svg viewBox="0 0 20 22"><path d="M4 2l4 4-2 3c1 3 3 6 6 8l3-2 4 4-3 3C8 21 1 12 1 5z" fill="#fff"/></svg>0400 123 987</div>
    <div class="contact__web"><svg viewBox="0 0 13 13"><circle cx="6.5" cy="6.5" r="6" fill="#fff"/></svg>www.lanternwellgroup.com.au</div>
  </div>
</section>

</body>
</html>
```